Spiritual Support flyer design

I offer a range of spiritual support options from a drop in group to meditation. I work alone in two locations, one at home and the other in the local town centre therapy centre. I do not want people to be confused about where to go for each item so thought one side could be the town centre group and the other side of the leaflet could be the things I offer from home. I need to find a way to present a list of things I do and make it look inviting so people want to contact me. I want it to feel inspirational, uplifting, light hearted, with a gentle feel of support or coming home to somewhere safe. The leaflet needs to look eye catching as it will be where there are many other leaflets the same size (A5). I love purples, as they tend to be spiritual colours or the look below of light bursting through the clouds seems appropriate picture wise. I do not have a logo.
The title can be Amber Lantern. On one side I would like to introduce a Spiritual Experiences drop-in group held at the Pebble Hall Centre, Colchester 1-2pm every four weeks to share spiritual experiences with others. I can give you more words for that when you are ready. The other side needs to feature the things I offer from my own home which are: Spiritual Counselling, Private email guidance, Meditation one to one, and Amber Lantern Days, which are like a days retreat. It might be a good idea to mention prices but not in an obvious way, so have that just readable in small print.

```html
<!DOCTYPE html>
<html lang="en">
<head>
<meta charset="utf-8">
<title>Amber Lantern – Spiritual Support Flyer</title>
<link href="https://fonts.googleapis.com/css2?family=Source+Sans+3:wght@400;600;700;800&display=swap" rel="stylesheet">
<style>
  :root{
    --backdrop:#000000;
    --plum:#6e1268;
    --plum-deep:#5e0f5c;
    --violet-band:#8e3f9c;
    --violet-light:#b06fc0;
    --sky-blue:#bfe6f8;
    --ink:#2a2a3a;
    --mist-grey:#c9c9c9;
    --white:#ffffff;
    --accent-pink:#8a2a90;
  }
  *{box-sizing:border-box;margin:0;padding:0}
  html,body{width:1200px;height:861px;overflow:hidden;background:var(--backdrop)}
  body{position:relative;font-family:"Source Sans 3",Arial,sans-serif;color:var(--ink)}

  .flyer-side{position:absolute;overflow:hidden}

  /* Drop-in group side */
  .group-side{left:37px;top:33px;width:557px;height:787px;background:var(--white)}
  .sky-backdrop{position:absolute;inset:0;
    background:
      radial-gradient(ellipse 70% 30% at 55% 20%, rgba(255,255,255,.95), rgba(255,255,255,0) 70%),
      radial-gradient(ellipse 60% 25% at 30% 75%, rgba(150,90,180,.55), rgba(150,90,180,0) 70%),
      linear-gradient(180deg,#e9e4f3 0%,#f5f3fa 30%,#d9cde9 55%,#b99ccf 72%,#e8e0f0 88%,#f4f1f8 100%);}
  .group-header{position:absolute;left:0;top:0;width:100%;height:127px;
    background:linear-gradient(90deg,var(--violet-band),var(--violet-light) 55%,var(--violet-band));
    color:var(--white);text-align:center}
  .group-title{position:absolute;left:0;right:0;top:40px;font-size:37px;font-weight:800;letter-spacing:.5px;line-height:1}
  .group-subtitle{position:absolute;left:0;right:0;top:82px;font-size:23px;font-weight:600;line-height:1}
  .group-body{position:absolute;left:70px;width:417px;text-align:center;font-size:15.5px;line-height:18.5px}
  .intro{top:186px}
  .intro p+p{margin-top:10px}
  .host-name{font-weight:700;color:var(--accent-pink)}
  .host-bio{font-size:14px;line-height:17.5px}
  .host-bio strong{font-weight:700;color:#111}
  .host-sally{top:364px}
  .host-lin{top:475px}
  .contact-note{margin-top:9px;color:var(--accent-pink)}
  .contact-detail{font-weight:600;color:#111}
  .venue{position:absolute;left:0;right:0;top:707px;text-align:center;color:var(--plum);font-size:15.5px;font-weight:600;line-height:19px}

  /* Home services side */
  .services-side{left:607px;top:33px;width:561px;height:791px;background:var(--white)}
  .top-band{position:absolute;left:0;top:0;width:100%;height:38px;background:var(--mist-grey)}
  .brand-name{position:absolute;left:0;right:0;top:56px;text-align:center;color:var(--plum);font-size:41px;font-weight:700;letter-spacing:.5px;line-height:1}
  .home-address{position:absolute;left:0;right:0;top:100px;text-align:center;font-size:14px;font-weight:700;line-height:18px;color:#222}

  .price-list{position:absolute;left:53px;top:156px;width:454px;border-collapse:collapse}
  .price-list th{background:var(--plum);color:var(--white);text-align:left;font-size:14px;font-weight:700;height:27px;padding:0 11px}
  .price-list td{background:var(--sky-blue);font-size:14px;line-height:17px;padding:0 11px;color:#222}
  .price-list .price{width:120px;color:var(--plum);font-size:24px;font-weight:700;padding-left:20px}
  .row-tall td{height:48px}
  .row-short td{height:28px}
  .row-last td{height:31px}

  .lotus-area{position:absolute;left:94px;top:435px;width:350px;height:185px;border-radius:50% 50% 40% 40%/60% 60% 40% 40%;
    background:radial-gradient(ellipse at 50% 45%,#e6e6e6,#bdbdbd 70%,rgba(255,255,255,0) 72%)}

  .booking-band{position:absolute;left:0;bottom:0;width:100%;height:156px;background:var(--plum-deep);color:var(--white)}
  .booking-row{position:absolute;left:97px;display:flex;align-items:center}
  .booking-label{width:142px;font-size:12px;font-weight:700}
  .booking-colon{width:47px;font-size:12px}
  .booking-value{font-size:16px;font-weight:600}
  .row-web{top:13px}
  .row-mail{top:40px}
  .row-phone{top:67px}
</style>
</head>
<body>

<section class="flyer-side group-side">
  <div class="sky-backdrop" role="img" aria-label="Soft purple sky with light bursting through the clouds"></div>
  <header class="group-header">
    <h1 class="group-title">SPIRITUAL EXPERIENCES</h1>
    <p class="group-subtitle">A drop-in group</p>
  </header>

  <div class="group-body intro">
    <p><span class="host-name">Mara and Jo</span> invite you to drop in and share any spiritual experiences you may have had, enlightened moments, or developing spiritual gifts, in a supportive environment.</p>
    <p>Perhaps you feel that you are the only one experiencing what you do and would like to talk about it, or listen to others experiences. In the group you can share with like-minded souls for personal development and inspiration.</p>
  </div>

  <div class="group-body host-bio host-sally">
    <p><strong>Mara Wells</strong> – has loved all things spiritual from an early age and provides email consultations, spiritual counselling, and amber lantern days</p>
    <p class="contact-note">Please contact us for future dates</p>
    <p class="contact-detail">mara.wells@example.com 01206 000123</p>
  </div>

  <div class="group-body host-bio host-lin">
    <p><strong>Jo Harlow</strong> – had a spiritual awakening and became open to angels, is sensitive to energies, and has been on a pathway of self-discovery ever since. She enjoys emotionally supporting others on their life journey.</p>
    <p class="contact-note">Please contact us for future dates</p>
    <p class="contact-detail">01206 000456&nbsp;&nbsp;jo.harlow@example.com</p>
  </div>

  <p class="venue">The Pebble Hall Centre, 7 Orchard Lane, Colchester<br>Contribution: £5</p>
</section>

<section class="flyer-side services-side">
  <div class="top-band"></div>
  <h2 class="brand-name">AMBER LANTERN</h2>
  <p class="home-address">@ The Meditation Room, 14 Willow Close,<br>Colchester CO0 0AA</p>

  <table class="price-list">
    <tr><th colspan="2">Spiritual Counselling</th></tr>
    <tr class="row-tall"><td>Up to an hours confidential one to<br>one support and assistance</td><td class="price">£45</td></tr>
    <tr><th colspan="2">Private email guidance</th></tr>
    <tr class="row-short"><td>Response within 24 hours or sooner</td><td class="price">£45</td></tr>
    <tr><th colspan="2">Meditation one to one</th></tr>
    <tr class="row-tall"><td>Beginners or advanced assistance to<br>develop your practice</td><td class="price">£45</td></tr>
    <tr><th colspan="2">Amber Lantern day</th></tr>
    <tr class="row-last"><td>A day learning to re-align with your inner being</td><td class="price">£90</td></tr>
  </table>

  <div class="lotus-area" role="img" aria-label="Silver lotus flower illustration"></div>

  <footer class="booking-band">
    <div class="booking-row row-web"><span class="booking-label">Please book on line at</span><span class="booking-colon">:</span><span class="booking-value">www.marawells.example</span></div>
    <div class="booking-row row-mail"><span class="booking-label">or email</span><span class="booking-colon">:</span><span class="booking-value">mara.wells@example.com</span></div>
    <div class="booking-row row-phone"><span class="booking-label">Telephone</span><span class="booking-colon">:</span><span class="booking-value">01206 000123</span></div>
  </footer>
</section>

</body>
</html>
```